New business card with our logo

we finalized our logo with the help of pixel harbor - now we need a business card using that logo. we are a metal service center providing raw steel and metal products for fabricating, contractors, artists, etc. we have the wording for the back of the card figured out (attached, no deviations from text please), just need help putting it all together.
would like the look of steel somehow incorporated in the design ... would like the black part of the logo to be steel or silver color (the S & BRANLEY)
Other font styles liked:
- calibri, arial, similar to those, modern looking
Colors
Designer to choose colors to be used in the design.
Requirements
Must have
- Back of card must haves are attached (no deviations from wording please).
- FRONT of card:
- logo
- address
- name
- office tel
- cell
- fax
- website
- address
Nice to have
- incorporate the look of steel or element of steel somehow
- names of the staff on front not in all caps, i.e. Rosvita not ROSVITA
- this industry is more industrial, not coffee or flower shop so design should be aligned with that
- design should be classic and tasteful

```html
<!DOCTYPE html>
<html lang="en">
<head>
<meta charset="utf-8">
<title>Branley Steel – Business Card</title>
<link href="https://fonts.googleapis.com/css2?family=Arimo:ital,wght@0,400;0,700;1,700&display=swap" rel="stylesheet">
<style>
  :root {
    --page: #ffffff;
    --ink: #000000;
    --white: #ffffff;
    --brand-blue: #1a78c2;
    --steel-edge: #6a6a6a;
    --steel-mid: #a8a8a8;
    --steel-light: #cbcbcb;
    --band: #000000;
  }
  * { margin: 0; padding: 0; box-sizing: border-box; }
  html, body { width: 1200px; height: 1000px; overflow: hidden; background: var(--page); }
  body { position: relative; font-family: "Arimo", Arial, sans-serif; }

  .card {
    position: absolute;
    width: 389px;
    height: 243px;
    overflow: hidden;
    background: linear-gradient(90deg, var(--steel-edge) 0%, var(--steel-mid) 10%, var(--steel-light) 42%, var(--steel-light) 55%, var(--steel-mid) 88%, var(--steel-edge) 100%);
  }
  .card--front { left: 143px; top: 379px; }
  .card--back { left: 556px; top: 380px; }

  .brand {
    position: absolute;
    top: 25px;
    left: 0;
    width: 100%;
    display: flex;
    justify-content: center;
    align-items: center;
    gap: 12px;
  }
  .brand__dot {
    width: 58px;
    height: 58px;
    border-radius: 50%;
    background: var(--brand-blue);
    flex: none;
  }
  .brand__name {
    font-weight: 700;
    font-size: 27px;
    letter-spacing: 0.5px;
    color: var(--brand-blue);
    white-space: nowrap;
  }

  .staff-name {
    position: absolute;
    top: 94px;
    width: 100%;
    text-align: center;
    font-weight: 700;
    font-size: 18px;
    color: var(--ink);
  }
  .contact {
    position: absolute;
    top: 153px;
    width: 100%;
    text-align: center;
    font-weight: 700;
    font-size: 12.5px;
    line-height: 17px;
    color: var(--ink);
    white-space: nowrap;
  }
  .front-band {
    position: absolute;
    left: 0; bottom: 0;
    width: 100%;
    height: 26px;
    background: var(--band);
  }

  .back-panel {
    position: absolute;
    left: 0; top: 104px;
    width: 100%;
    height: 139px;
    background: var(--band);
    color: var(--white);
    text-align: center;
    font-weight: 700;
  }
  .back-panel__title { position: absolute; top: 5px; width: 100%; font-size: 20px; }
  .back-panel__services { position: absolute; top: 30px; width: 100%; font-size: 13px; }
  .back-panel__rule { position: absolute; top: 53px; left: 34px; width: 314px; height: 2px; background: var(--brand-blue); }
  .back-panel__products { position: absolute; top: 60px; width: 100%; font-size: 13px; line-height: 16px; }
  .back-panel__tagline { position: absolute; top: 101px; width: 100%; font-size: 14.5px; font-style: italic; }
  .sep { font-size: 9px; vertical-align: 2px; padding: 0 3px; }
</style>
</head>
<body>
  <section class="card card--front">
    <div class="brand">
      <span class="brand__dot"></span>
      <span class="brand__name">BRANLEY STEEL</span>
    </div>
    <p class="staff-name">Rosvita</p>
    <div class="contact">
      <p>Address.................................................................</p>
      <p>Office tel:............&nbsp;&nbsp; Cell:...................Fax:.................</p>
      <p>Email:..................&nbsp; Website:.......................................</p>
    </div>
    <div class="front-band"></div>
  </section>

  <section class="card card--back">
    <div class="brand">
      <span class="brand__dot"></span>
      <span class="brand__name">BRANLEY STEEL</span>
    </div>
    <div class="back-panel">
      <p class="back-panel__title">METAL SERVICE CENTER</p>
      <p class="back-panel__services">CUT&nbsp; SHEAR<span class="sep">■</span>PUNCH<span class="sep">■</span>LIGHT FAB</p>
      <div class="back-panel__rule"></div>
      <div class="back-panel__products">
        <p>Structural Steel<span class="sep">■</span>Stainless &amp; Aluminium</p>
        <p>Building Components<span class="sep">■</span>Rebar <span class="sep">■</span>Decking ...and more!</p>
      </div>
      <p class="back-panel__tagline">Cut to size, Pick-up or Delivered!</p>
    </div>
  </section>
</body>
</html>
```